PELUNDOM Auto Battery

We need top of the line design for a new product that we are launching, Automotive Batteries.
We are an exporter of Auto Spare parts based in China, our new products will be launched in October 2012, the website is to be presented as B2B not B2C, we deal directly with Importers all around the world.
Our vision for the website is to be Clean, elegant, smart, warm, reflects confidence and trust..therefore, the choice of themes, colors, fonts and graphics should take into considerations all above.
Since there are hundreds of Battery types, specs, sizes, weight...etc, we will need a upload template that will enable us to upload, modify and manipulate the data of the batteries.
Car battery importers
Automotive

```html
<!DOCTYPE html>
<html lang="en">
<head>
<meta charset="utf-8">
<title>PELUNDOM Auto Battery</title>
<link rel="stylesheet" href="https://fonts.googleapis.com/css2?family=Dosis:wght@500;600&family=PT+Sans:wght@400;700&display=swap">
<style>
  :root {
    --ink: #1c1c1c;
    --header-top: #ffffff;
    --header-bottom: #dedede;
    --brick-top: #c95c4a;
    --brick-bottom: #a82e1e;
    --nav-top: #d25a45;
    --nav-bottom: #b2321f;
    --nav-active-top: #e2735e;
    --nav-active-bottom: #c8503c;
    --nav-divider: #9a2615;
    --white: #ffffff;
    --card-photo: #f4f4f4;
    --card-band-top: #000000;
    --card-band-bottom: #2a2a2a;
    --card-label: #d8d8d8;
    --footer: #121212;
  }
  * { margin: 0; padding: 0; box-sizing: border-box; }
  html, body { width: 1200px; height: 955px; overflow: hidden; }
  body {
    position: relative;
    font-family: "PT Sans", "Myriad Pro", sans-serif;
    color: var(--white);
    background: linear-gradient(180deg, var(--brick-top) 181px, var(--brick-bottom) 923px);
  }
  .site-header {
    position: absolute; left: 0; top: 0; width: 1200px; height: 181px;
    background: linear-gradient(180deg, var(--header-top), var(--header-bottom));
  }
  .brand {
    position: absolute; left: 0; top: 38px; width: 1200px; text-align: center;
    font-family: "Dosis", sans-serif; color: var(--ink); font-weight: 500;
  }
  .brand-name { display: block; font-size: 44px; line-height: 48px; letter-spacing: 1px; }
  .brand-tagline { display: block; font-size: 27px; line-height: 30px; margin-top: 0; }
  .main-nav {
    position: absolute; left: 145px; top: 131px; width: 913px; height: 70px;
    display: flex; list-style: none;
    background: linear-gradient(180deg, var(--nav-top), var(--nav-bottom));
    box-shadow: 0 3px 6px rgba(0,0,0,0.35);
    border-radius: 3px;
  }
  .main-nav li {
    display: flex; align-items: center; justify-content: center;
    font-size: 18.5px; color: var(--white);
    border-right: 1px solid var(--nav-divider);
  }
  .main-nav li:last-child { border-right: none; }
  .main-nav li.is-active { background: linear-gradient(180deg, var(--nav-active-top), var(--nav-active-bottom)); }
  .feature-cards { position: absolute; left: 166px; top: 266px; width: 877px; height: 340px; }
  .feature-card {
    position: absolute; top: 0; width: 288px; height: 340px;
    border-radius: 9px; overflow: hidden; background: var(--card-photo);
  }
  .feature-photo { width: 288px; height: 282px; }
  .feature-label {
    height: 58px; display: flex; align-items: center; justify-content: center;
    background: linear-gradient(180deg, var(--card-band-top), var(--card-band-bottom));
    font-family: "Dosis", sans-serif; font-weight: 500; font-size: 39px; color: var(--card-label);
  }
  .slider-dots { position: absolute; left: 950px; top: 620px; }
  .welcome-title {
    position: absolute; left: 0; top: 656px; width: 1200px; text-align: center;
    font-family: "Dosis", sans-serif; font-weight: 600; font-size: 34px; line-height: 44px;
    text-shadow: 0 2px 3px rgba(0,0,0,0.45);
  }
  .welcome-text {
    position: absolute; left: 166px; top: 705px; width: 900px;
    font-size: 18.5px; line-height: 37.2px;
  }
  .site-footer {
    position: absolute; left: 0; top: 923px; width: 1200px; height: 32px;
    background: var(--footer); font-size: 13px;
  }
  .copyright { position: absolute; left: 169px; top: 8px; }
  .legal-link { position: absolute; right: 177px; top: 8px; }
</style>
</head>
<body>
  <header class="site-header">
    <div class="brand">
      <span class="brand-name">PELUNDOM</span>
      <span class="brand-tagline">Auto Battery</span>
    </div>
  </header>

  <ul class="main-nav">
    <li class="is-active" style="width:139px">Home</li>
    <li style="width:144px">About Us</li>
    <li style="width:146px">Products</li>
    <li style="width:138px">Services</li>
    <li style="width:167px">Our Clients</li>
    <li style="width:179px">Contact Us</li>
  </ul>

  <section class="feature-cards">
    <article class="feature-card" style="left:0">
      <div class="feature-photo" role="img" aria-label="Product photo of a white car battery with a red label" style="background:radial-gradient(ellipse at 50% 50%, #d8d2cf 0%, #e9e4e2 35%, #f4f4f4 70%)"></div>
      <div class="feature-label">Solution</div>
    </article>
    <article class="feature-card" style="left:294px">
      <div class="feature-photo" role="img" aria-label="Photo of two business people shaking hands" style="background:linear-gradient(90deg, #f4f4f4 0%, #2a3550 12%, #b9896a 40%, #8a5a40 60%, #2a3550 88%, #f4f4f4 100%); background-size:100% 40%; background-repeat:no-repeat; background-position:0 45%; background-color:var(--card-photo)"></div>
      <div class="feature-label">Bonding</div>
    </article>
    <article class="feature-card" style="left:589px">
      <div class="feature-photo" role="img" aria-label="Illustration of a silver world map on a blue background" style="background:radial-gradient(ellipse at 50% 48%, #4c6585 0%, #8396ae 45%, #f4f4f4 78%)"></div>
      <div class="feature-label">Expand</div>
    </article>
  </section>

  <svg class="slider-dots" width="96" height="28" viewBox="0 0 96 28" aria-hidden="true">
    <circle cx="14" cy="14" r="9.5" fill="#ffffff" stroke="#f0b0a3" stroke-width="2.5"/>
    <circle cx="43" cy="14" r="9.5" fill="none" stroke="#f0b0a3" stroke-width="2.5"/>
    <circle cx="71" cy="14" r="9.5" fill="none" stroke="#f0b0a3" stroke-width="2.5"/>
  </svg>

  <h1 class="welcome-title">Welcome to our site</h1>
  <div class="welcome-text">
    <p>We need top of the line design for a new product that we are launching, Automotive Batteries.</p>
    <p>We are an exporter of Auto Spare parts based in China, our new products will be launched in October 2012,</p>
    <p>the website is to be presented as B2B not B2C, we deal directly with Importers all around the world.</p>
    <p>Our vision for the website is to be Clean, elegant, smart, warm, reflects confidence and trust..therefore, the</p>
    <p>choice of themes, colors, fonts and graphics should take into considerations all above.</p>
  </div>

  <footer class="site-footer">
    <span class="copyright">Copyright @ 2012, PELUNDOM</span>
    <span class="legal-link">Terms &amp; Privacy Policy</span>
  </footer>
</body>
</html>
```